serious, thorough, light and simple - that's my advice and mediations

My business card should combine my logo (uploaded file) and my homepage (https://fellor-mediation.webnestsite.com).

Contact Information for Business Card

Name: Sabine Fellor di Vanti
Phone: 076 412 58 94
mail: sfellor@postkiv.ch
web: www.fellor-di-vanti.ch

```html
<!DOCTYPE html>
<html lang="de">
<head>
<meta charset="utf-8">
<title>Wege im Dialog – Visitenkarte</title>
<link rel="stylesheet" href="https://fonts.googleapis.com/css2?family=Montserrat:wght@400;500&display=swap">
<style>
  :root {
    --bg: #e4e5e8;
    --green-dark: #00572e;
    --green-light: #00784b;
    --green-text: #0b6b35;
    --gold: #a8803f;
    --ink: #2a2a2a;
    --navy: #27357a;
    --rule: #9a9a9a;
    --paper: #ffffff;
  }
  * { margin: 0; padding: 0; box-sizing: border-box; }
  html, body {
    width: 1200px;
    height: 800px;
    overflow: hidden;
    background: var(--bg);
    font-family: "Montserrat", sans-serif;
  }
  .canvas {
    position: relative;
    width: 1200px;
    height: 800px;
  }
  .card {
    position: absolute;
    left: 389px;
    width: 461px;
    height: 263px;
  }
  .card--front {
    top: 93px;
    background: linear-gradient(60deg, var(--green-dark) 0%, var(--green-light) 100%);
    display: flex;
    align-items: center;
    justify-content: center;
  }
  .card--back {
    top: 422px;
    background: var(--paper);
  }
  .brand__name {
    color: var(--gold);
    font-weight: 500;
    white-space: nowrap;
  }
  .card--front .brand__name { font-size: 32px; }

  .card--back .brand {
    position: absolute;
    left: 57px;
    top: 112px;
    width: 164px;
    text-align: center;
  }
  .card--back .brand__name { font-size: 19px; line-height: 24px; }

  .divider {
    position: absolute;
    left: 235px;
    top: 70px;
    width: 1px;
    height: 122px;
    background: var(--rule);
  }
  .contact {
    position: absolute;
    left: 251px;
    top: 70px;
    color: var(--ink);
  }
  .contact__name {
    color: var(--green-text);
    font-size: 14.5px;
    font-weight: 500;
    line-height: 18px;
  }
  .contact__role { font-size: 10px; line-height: 14px; margin-top: 2px; }
  .contact__label {
    color: var(--gold);
    font-size: 12.5px;
    line-height: 16px;
    margin-top: 9px;
  }
  .contact__homepage { font-size: 10.5px; line-height: 14px; margin-top: 1px; }
  .contact__list { list-style: none; margin-top: 11px; }
  .contact__item {
    display: flex;
    align-items: center;
    gap: 5px;
    font-size: 10.5px;
    line-height: 14px;
  }
  .contact__icon { width: 8px; height: 8px; flex: none; fill: var(--navy); }
</style>
</head>
<body>
<main class="canvas">
  <section class="card card--front" aria-label="Vorderseite">
    <div class="brand">
      <span class="brand__name">Wege im Dialog</span>
    </div>
  </section>

  <section class="card card--back" aria-label="Rückseite">
    <div class="brand">
      <span class="brand__name">Wege im Dialog</span>
    </div>
    <div class="divider"></div>
    <div class="contact">
      <p class="contact__name">Sabine Fellor di Vanti</p>
      <p class="contact__role">CEO</p>
      <p class="contact__label">Homepage</p>
      <p class="contact__homepage">fellor-mediation.webnestsite.com</p>
      <ul class="contact__list">
        <li class="contact__item">
          <svg class="contact__icon" viewBox="0 0 10 10" aria-hidden="true"><path d="M2 0.5 L3.6 0.5 L4.2 2.8 L3.1 3.6 Q4 5.8 6.4 6.9 L7.2 5.8 L9.5 6.4 L9.5 8 Q9.3 9.5 7.8 9.5 Q0.5 8.8 0.5 2 Q0.5 0.6 2 0.5 Z"/></svg>
          076 412 58 94
        </li>
        <li class="contact__item">
          <svg class="contact__icon" viewBox="0 0 10 10" aria-hidden="true"><path d="M0.5 2 H9.5 V8.5 H0.5 Z M1 2.4 L5 5.6 L9 2.4" stroke="#fff" stroke-width="0.8"/></svg>
          sfellor@postkiv.ch
        </li>
        <li class="contact__item">
          <svg class="contact__icon" viewBox="0 0 10 10" aria-hidden="true"><circle cx="5" cy="5" r="4.5"/><path d="M0.5 5 H9.5 M5 0.5 V9.5 M1.3 2.8 H8.7 M1.3 7.2 H8.7" stroke="#fff" stroke-width="0.6" fill="none"/><ellipse cx="5" cy="5" rx="2" ry="4.5" stroke="#fff" stroke-width="0.6" fill="none"/></svg>
          www.fellor-di-vanti.ch
        </li>
      </ul>
    </div>
  </section>
</main>
</body>
</html>
```